Doctor to Patient Management Website

I need a design for a health management website that connects doctors to patients. The website will consist of: A main page mainly describing our goal, services, and initiatives towards (Who we are AKA "About Us", Our services, Contact Us, Quick Links for health tips, Language selection, Find a doctor, search bar, Member Login Section, small glossary section below with links to all entities mentioned prior, Help section (Helpful tips and tutorials, Used to request help from admin, customer service, to resolve issues or get assistance). A profile page with two types:1) Doctor Profile: Doctor Personal info (First, Last, Middle Name, Title), Clinic, Hospital Info, Department, Credentials, Years of Experience, Patients rating, #Patients seen during the current week, #Patients seen in total, Picture, Link to email doctor, Link to print doctor's profile). Tabs for "About Me", "Contact Info", "Ratings & Comments", "Documents" (To be downloaded and uploaded by patient), "Patients (List of Patients alphabetical order by name)", "Calendar" (to see doctor's availability for booking) underneath all links. 2) Patient profile: About me, Personal Info, Height, Weight, Blood Type, Age, DOB, Name, etc..., Message and email link.Picture of patient with menu made of "Personal Data", "Biometrics", "Allergies", "Illnesses", "Medications", "Medical Procedures", "Doctors" treating the patient, "Documents" (To be downloaded and uploaded by patient). Underneath all, other patients he or she is related to (For example: family member, so patient can't connect to other patients who are family members)3) Login section: New Users will have option to register using:First Name (Required), Last Name, Middle (not required), Address (Not required), City (Required), Country (Required), Email (Not required), Phone Number (Required), Choose UserName, Password, Account Type (Doctor or Patient). Once registered, they will log in using UserName, Password, and Account_Type.Curent Users will log in using UserName, Password, and Account_Type and option to retrieve username or password.Pages to include (Login Page - Registration Page - Retrieve Username and Reset Password Page)Please see link below:https://lanternpost-media.example/importance-claiming-vitalrank-quopa-zeltra/Pictures are attached to this project as an inspirationFYI: Dummy text can be used to fill in the business, services, and descriptive information. Feel free to include your own ideas in the layout, design, categories, patterns, and more to and showcase your talent. Design and pictures provided are available as source of ideas.

Target Market(s)

Age: 21+ / Family Oriented / Medical Sector / Metropolitan Area / Educated and non Educated Users

Industry/Entity Type

Health Care

Number of Pages Required

5+ page

Font styles to use
Sans Serif

Colors

Designer to choose colors to be used in the design.

Requirements
Must have
• Thin layer design
• Simple font - No serif
• Clean menu with light but solid colors (No Gradient effect)
Nice to have
• Different color themes (2 or 3) can be combined
• Sample pictures for illustration (either as an ad or to go with the flow of your design)
• Dashboard Feel (Suggested but not required)
Should not have
• Artistic fonts - with Serif
• Dark color themes

```html
<!DOCTYPE html>
<html lang="en">
<head>
<meta charset="utf-8">
<title>Carewell – Find a Doctor</title>
<link rel="stylesheet" href="https://fonts.googleapis.com/css2?family=Raleway:wght@400;500;600;700&family=Open+Sans:wght@400;600;700&display=swap">
<style>
:root{
  --purple:#463e7c;
  --purple-dark:#3b3469;
  --teal:#6ccdc0;
  --teal-footer:#3fc2b0;
  --teal-mid:#37b5a3;
  --teal-deep:#2fa896;
  --coral:#f25f5c;
  --ink:#222222;
  --text:#555555;
  --muted:#999999;
  --white:#ffffff;
  --bar:#1f1f1f;
}
*{margin:0;padding:0;box-sizing:border-box}
html,body{width:1200px;height:2334px;overflow:hidden}
body{font-family:"Open Sans",Arial,sans-serif;color:var(--text);background:var(--white);position:relative}
.abs{position:absolute}
h1,h2,h3,.raleway{font-family:"Raleway",Arial,sans-serif}

/* header */
.site-header{position:absolute;left:0;top:0;width:1200px;height:120px;background:var(--white)}
.help-tab{position:absolute;left:808px;top:6px;width:261px;height:37px;background:var(--coral);
  clip-path:polygon(0 0,100% 0,100% 100%,0 100%,14px 50%);display:flex;align-items:center;justify-content:flex-end;gap:26px;padding-right:18px;color:var(--white);font-size:11px}
.help-tab .caret{display:inline-block;width:0;height:0;border-left:5px solid transparent;border-right:5px solid transparent;border-top:6px solid var(--white);margin-left:8px;vertical-align:middle}
.brand{position:absolute;left:131px;top:59px;display:flex;align-items:center;gap:4px;font-family:"Raleway",sans-serif;font-weight:600;font-size:25px;letter-spacing:3px;color:#333}
.brand .mark{width:31px;height:31px;background:#333}
.main-nav{position:absolute;top:67px;left:0;font-size:15px;color:#444}
.main-nav span{position:absolute;white-space:nowrap}
.nav-caret{display:inline-block;width:7px;height:7px;border-right:1.5px solid #444;border-bottom:1.5px solid #444;transform:rotate(45deg);margin-left:12px;position:relative;top:-3px}
.btn{display:flex;align-items:center;justify-content:center;background:var(--teal);color:var(--white);border-radius:3px;font-family:"Raleway",sans-serif}
.signup-btn{left:981px;top:59px;width:86px;height:34px;font-size:15px}

/* hero */
.hero{position:absolute;left:0;top:120px;width:1200px;height:448px;background:var(--purple);overflow:hidden}
.hero-art{position:absolute;border-radius:30px;background:linear-gradient(160deg,rgba(255,255,255,.12),rgba(109,205,192,.12))}
.hero-title{position:absolute;left:0;width:1200px;top:122px;text-align:center;color:var(--white);font-size:49px;font-weight:700;letter-spacing:.5px}
.hero-text{position:absolute;left:350px;width:528px;top:190px;text-align:center;color:#e4e2f0;font-size:13px;line-height:19px}
.search{position:absolute;left:365px;top:258px;width:501px;height:44px;background:var(--white);border-radius:3px;overflow:hidden;box-shadow:0 2px 6px rgba(0,0,0,.15)}
.search .placeholder{position:absolute;left:20px;top:14px;font-size:11px;color:#aaa}
.search .go{position:absolute;right:0;top:0;width:106px;height:44px;background:var(--teal);color:var(--white);font-size:14px;font-weight:700;display:flex;align-items:center;justify-content:center;letter-spacing:.5px}
.filter{position:absolute;top:328px;height:22px;font-size:11px;font-weight:700;color:var(--white);display:flex;align-items:center;justify-content:center;background:#1f1b33;border-radius:2px}
.filter.active{background:var(--teal)}

/* about */
.about-art{position:absolute;left:128px;top:608px;width:464px;height:336px;border-radius:24px;background:linear-gradient(180deg,#eef3fb,#cfd6f3)}
.about-title{position:absolute;left:621px;top:668px;font-size:29px;font-weight:400;color:var(--ink);letter-spacing:.5px}
.about-title b,.tips-title b{font-weight:700}
.about-text{position:absolute;left:621px;top:718px;width:440px;font-size:11.5px;line-height:16.3px;color:#444}
.readmore-btn{left:622px;top:856px;width:125px;height:42px;font-size:15px}

/* testimonial */
.testimonial{position:absolute;left:0;top:970px;width:1200px;height:499px;background:linear-gradient(120deg,#5b5e78 0%,#434763 45%,#2f3246 75%,#4c5670 100%)}
.testi-title{position:absolute;left:100px;width:492px;top:72px;text-align:center;color:var(--white);font-size:36px;font-weight:700;line-height:44px}
.quote-mark{position:absolute;color:var(--teal);font-size:60px;font-family:Georgia,serif;font-weight:700;line-height:1}
.quote-text{position:absolute;left:160px;width:404px;top:198px;text-align:center;color:var(--white);font-size:14px;line-height:16.5px}
.avatar{position:absolute;left:333px;top:299px;width:70px;height:70px;border-radius:50%;background:linear-gradient(180deg,#f1d8b4,#e7c9a8);border:3px solid var(--white)}
.testi-name{position:absolute;left:100px;width:540px;top:384px;text-align:center;color:var(--white);font-size:18px;font-weight:700;font-family:"Raleway",sans-serif}
.dots{position:absolute;left:352px;top:430px;display:flex;gap:3px}
.dots i{display:block;width:7px;height:7px;border-radius:50%;background:var(--white)}
.dots i.on{background:var(--teal)}

.login-box{position:absolute;left:626px;top:57px;width:420px;height:383px;border:2px solid var(--white);border-radius:3px;background:rgba(30,32,48,.35)}
.tab{position:absolute;top:25px;height:45px;display:flex;align-items:center;justify-content:center;font-size:19px;color:var(--white)}
.tab.active{left:23px;width:187px;background:var(--teal)}
.tab.plain{left:210px;width:182px;border:2px solid var(--white);border-left:none}
.field{position:absolute;left:23px;width:369px;border:2px solid var(--white);color:var(--white);font-size:13px;font-weight:600;padding-left:16px;display:flex;align-items:center}
.field .sel{position:absolute;right:14px;top:50%;margin-top:-3px;border-left:7px solid transparent;border-right:7px solid transparent;border-top:8px solid var(--white)}
.forgot{position:absolute;left:27px;top:312px;font-size:11px;color:var(--coral)}
.login-btn{left:270px;top:302px;width:125px;height:43px;font-size:16px}

/* health tips */
.tips{position:absolute;left:0;top:1469px;width:1200px;height:646px;background:#fbfbfc}
.tips-title{position:absolute;left:0;width:1200px;top:48px;text-align:center;font-size:29px;font-weight:400;color:var(--ink)}
.tips-text{position:absolute;left:350px;width:500px;top:107px;text-align:center;font-size:13px;line-height:19px;color:#444}
.card{position:absolute;top:171px;width:258px;height:344px;background:var(--white);box-shadow:0 2px 8px rgba(0,0,0,.12)}
.card .photo{height:200px}
.card h3{position:absolute;left:22px;top:214px;font-size:18px;font-weight:500;color:var(--ink)}
.card p{position:absolute;left:22px;top:244px;width:215px;font-size:12px;line-height:15.5px;color:#555}
.card .meta{position:absolute;left:22px;right:22px;top:318px;font-size:10px;color:var(--muted);display:flex;justify-content:space-between}
.arrow-box{position:absolute;top:299px;width:38px;height:56px;background:#eeeeee;display:flex;align-items:center;justify-content:center}
.viewall-btn{left:539px;top:547px;width:125px;height:42px;font-size:15px}

/* social band & footer */
.social{position:absolute;left:0;top:2115px;width:1200px;height:58px;background:var(--purple)}
.social .label{position:absolute;left:131px;top:19px;font-size:14px;color:var(--white)}
.social .dot{position:absolute;top:21px;width:16px;height:16px;border-radius:50%;background:var(--white)}
.footer{position:absolute;left:0;top:2173px;width:1200px;height:136px}
.fcol{position:absolute;top:0;height:136px;color:var(--white);text-align:center}
.fcol h4{font-family:"Raleway",sans-serif;font-size:18px;font-weight:600;margin-top:40px;letter-spacing:.3px}
.fcol p{font-size:14px;line-height:17px;margin-top:12px}
.footer-brand{position:absolute;left:131px;top:51px;display:flex;align-items:center;gap:5px;font-family:"Raleway",sans-serif;font-weight:500;font-size:26px;letter-spacing:4px;color:var(--white)}
.footer-brand .mark{width:34px;height:34px;background:rgba(255,255,255,.55)}
.bottom-bar{position:absolute;left:0;top:2309px;width:1200px;height:25px;background:var(--bar);color:var(--white);font-size:9px;font-style:normal}
.bottom-bar .l{position:absolute;left:131px;top:7px}
.bottom-bar .r{position:absolute;right:131px;top:7px}
</style>
</head>
<body>

<header class="site-header">
  <div class="help-tab"><span>Tutorials</span><span>Quick Help</span><span>Language<i class="caret"></i></span></div>
  <div class="brand"><span class="mark"></span>CAREWELL</div>
  <nav class="main-nav">
    <span style="left:404px">Home</span>
    <span style="left:492px">About Us</span>
    <span style="left:600px">Our Services<i class="nav-caret"></i></span>
    <span style="left:757px">Health Tips<i class="nav-caret"></i></span>
    <span style="left:890px">
      <svg width="11" height="13" viewBox="0 0 11 13" style="vertical-align:-1px;margin-right:10px"><rect x="1" y="6" width="9" height="6.5" rx="1" fill="none" stroke="#444" stroke-width="1.3"/><path d="M3 6V4a2.5 2.5 0 0 1 5 0v2" fill="none" stroke="#444" stroke-width="1.3"/></svg>Login</span>
  </nav>
  <div class="btn abs signup-btn">Sign Up</div>
</header>

<section class="hero">
  <div class="hero-art" role="img" aria-label="Illustration of a stethoscope with pill strips and medicine bottles" style="left:40px;top:-20px;width:340px;height:460px"></div>
  <div class="hero-art" role="img" aria-label="Illustration of syringes, test tubes, pills and a medical clipboard" style="left:830px;top:0;width:370px;height:440px"></div>
  <h1 class="hero-title">FIND A DOCTOR</h1>
  <p class="hero-text">Lorem ipsum dolor sit amet, sit placerat aptent nec ornare ut morbi, suscipit accumsan, rhoncus quis, tincidunt morbi, mauris massa porttitor feugiat</p>
  <div class="search"><span class="placeholder">Search by condition, speciality or name</span><span class="go">SEARCH</span></div>
  <div class="filter active" style="left:514px;width:70px">All</div>
  <div class="filter" style="left:592px;width:70px">Clinics</div>
  <div class="filter" style="left:670px;width:71px">Doctors</div>
</section>

<section class="about">
  <div class="about-art" role="img" aria-label="Illustration of two patients and a doctor sitting on a sofa talking, holding a heart"></div>
  <h2 class="about-title">ABOUT <b>US</b></h2>
  <p class="about-text">Lorem ipsum dolor sit amet, blandit placerat mauris luctus bibendum dolor ac, nulla sit quam, nibh cras amet cursus pulvinar justo, et urna et, lacus sed nisl. Molestie iaculis diam scelerisque, eget risus mi.<br>Magna morbi integer pellentesque, turpis dui duis tellus fusce, nibh pretium vehicula pharetra, vel eget varius donec, eu donec tempus praesent lacus amet. Sed litora. Vel donec mauris, metus massa nam sit enim quam. Sapien id ultricies, lacinia ipsum sodales id condimentum.</p>
  <div class="btn abs readmore-btn">Read More</div>
</section>

<section class="testimonial" role="img" aria-label="Blurred photo of a doctor's desk with a laptop, glasses and stethoscope">
  <h2 class="testi-title">DONT TAKE OUR WORD<br>FOR IT !</h2>
  <span class="quote-mark" style="left:130px;top:150px">&ldquo;</span>
  <p class="quote-text">Lorem ipsum dolor sit amet, nulla magna, quam risus placerat morbi pede saepe cursus, ac etiam in voluptatem lacinia. Sit nec cursus curabitur iusto, dictumst vehicula ad velit metus, aliquam lorem facilisis pharetra</p>
  <span class="quote-mark" style="left:542px;top:256px">&rdquo;</span>
  <div class="avatar" role="img" aria-label="Portrait photo of the reviewer"></div>
  <div class="testi-name">DANA WHITFIELD</div>
  <div class="dots"><i></i><i class="on"></i><i class="on"></i></div>

  <div class="login-box">
    <div class="tab active">Sign In</div>
    <div class="tab plain">Sign Up</div>
    <div class="field" style="top:101px;height:48px">Account Type<i class="sel"></i></div>
    <div class="field" style="top:166px;height:47px">User Name*</div>
    <div class="field" style="top:230px;height:48px">Password</div>
    <span class="forgot">Forget password ?</span>
    <div class="btn abs login-btn">Log In</div>
  </div>
</section>

<section class="tips">
  <h2 class="tips-title">HEALTH <b>TIPS</b></h2>
  <p class="tips-text">Lorem ipsum dolor sit amet, sit placerat aptent nec ornare ut morbi, suscipit accumsan, rhoncus quis, tincidunt morbi, mauris massa porttitor feugiat</p>

  <div class="arrow-box" style="left:133px"><svg width="10" height="16" viewBox="0 0 10 16"><path d="M8 2 2 8l6 6" fill="none" stroke="#888" stroke-width="1.5"/></svg></div>
  <div class="arrow-box" style="left:1029px"><svg width="10" height="16" viewBox="0 0 10 16"><path d="M2 2l6 6-6 6" fill="none" stroke="#888" stroke-width="1.5"/></svg></div>

  <article class="card" style="left:190px">
    <div class="photo" role="img" aria-label="Photo of toy dentures biting a doughnut" style="background:linear-gradient(135deg,#bfe8ec,#e2463f)"></div>
    <h3>LOREM IPSUM</h3>
    <p>donec morbi lectus ac in id nunc, turpis aliquet velit, metus mollis potenti tortor tortor at. Neque litora sodales dictumst ridiculus mi</p>
    <div class="meta"><span>Read More &rarr;</span><span>(17 Reviews)</span></div>
  </article>
  <article class="card" style="left:474px">
    <div class="photo" role="img" aria-label="Photo of fresh carrots, beetroot and turnips" style="background:linear-gradient(135deg,#6f8a4a,#c8673a 55%,#7a2e3c)"></div>
    <h3>LOREM IPSUM</h3>
    <p>donec morbi lectus ac in id nunc, turpis aliquet velit, metus mollis potenti tortor tortor at. Neque litora sodales dictumst ridiculus mi</p>
    <div class="meta"><span>Read More &rarr;</span><span>(13 Reviews)</span></div>
  </article>
  <article class="card" style="left:755px">
    <div class="photo" role="img" aria-label="Photo of a hand resting among scattered pills" style="background:linear-gradient(135deg,#6b5e57,#c9b7ab)"></div>
    <h3>LOREM IPSUM</h3>
    <p>donec morbi lectus ac in id nunc, turpis aliquet velit, metus mollis potenti tortor tortor at. Neque litora sodales dictumst ridiculus mi</p>
    <div class="meta"><span>Read More &rarr;</span><span>(06 Reviews)</span></div>
  </article>

  <div class="btn abs viewall-btn">View All</div>
</section>

<section class="social">
  <span class="label">Get connected with us on social networks</span>
  <span class="dot" style="left:662px"></span>
  <span class="dot" style="left:736px"></span>
  <span class="dot" style="left:811px"></span>
  <span class="dot" style="left:891px"></span>
  <span class="dot" style="left:971px"></span>
  <span class="dot" style="left:1050px"></span>
</section>

<footer class="footer">
  <div class="fcol" style="left:0;width:363px;background:var(--teal-footer)"></div>
  <div class="footer-brand"><span class="mark"></span>CAREWELL</div>
  <div class="fcol" style="left:363px;width:237px;background:var(--teal-mid)"><h4>LOCATION</h4><p>24 Alder Lane, Brookfield,<br>Eastmoor E12</p></div>
  <div class="fcol" style="left:600px;width:234px;background:var(--teal-footer)"><h4>EMAIL ADDRESS</h4><p>info@carewell-clinic.example</p></div>
  <div class="fcol" style="left:834px;width:366px;background:var(--teal-deep)"><h4 style="padding-right:140px">CALL US</h4><p style="padding-right:140px">+00 555 010 482</p></div>
</footer>

<div class="bottom-bar"><span class="l">&copy; 2019 &nbsp;| &nbsp;All Right Reserved.</span><span class="r">Terms and Condition Apply &nbsp; | &nbsp; Privacy Policy</span></div>

</body>
</html>
```